Modern IT Cloud Services Company
(no text needed, only logo and contact info)
Modern IT Cloud Services Company - Information Technology
Creative Brief
Professional
Ravi Mehlan
President & CEO
2450 Birch Avenue Ste. 214 Naperville, IL 60563
800-517-9083 x416
rvmehlan@dorvaskell.com
www.nimbratek.com
We are open to using the font from the logo or a complimentary font. We would like to use a similar color scheme as the logo. We only want the website on the back of the card (not on the front). Please leave room in the corners if we want to print "rounded corner" business cards.

```html
<!DOCTYPE html>
<html lang="en">
<head>
<meta charset="utf-8">
<title>Nimbratek Stationery</title>
<link href="https://fonts.googleapis.com/css2?family=Montserrat:wght@400;600;700&display=swap" rel="stylesheet">
<style>
:root{
  --navy:#1d3f9c;
  --green:#3fb24a;
  --paper:#ffffff;
  --ink:#3b3f4a;
  --muted:#b9bfcc;
  --stage:#3d3d3f;
}
*{box-sizing:border-box;margin:0;padding:0}
html,body{width:1200px;height:254px;overflow:hidden;background:var(--stage);font-family:"Montserrat",sans-serif;color:var(--ink)}
.sheet-set{display:flex;gap:14px;padding:21px 16px;height:254px;align-items:flex-start}
.col{display:flex;flex-direction:column;gap:10px}
.row{display:flex;gap:8px}
.brand{display:flex;align-items:center;gap:4px;font-weight:700;color:var(--navy);letter-spacing:.2px;white-space:nowrap}
.brand .dot{width:.9em;height:.9em;border-radius:50%;background:var(--green);flex:none}
.brand.light{color:var(--paper)}

.letterhead{width:150px;height:212px;background:var(--paper);position:relative;padding:12px;overflow:hidden}
.letterhead .brand{font-size:12px}
.letterhead .body{margin-top:24px;display:flex;flex-direction:column;gap:5px}
.letterhead .line{height:2px;background:var(--muted)}
.letterhead .line.short{width:55%}
.letterhead .footer{position:absolute;left:0;right:0;bottom:0;height:22px;background:var(--navy);border-top:3px solid var(--green);color:var(--paper);font-size:5px;padding:3px 10px;line-height:1.4;white-space:nowrap}

.envelope{width:240px;height:112px;background:var(--paper);position:relative;padding:10px}
.envelope .brand{font-size:11px}
.envelope .return{font-size:5.5px;margin-top:3px;line-height:1.4}
.envelope .band{position:absolute;left:0;right:0;bottom:0;height:14px;background:var(--navy);border-top:3px solid var(--green)}

.card{width:116px;height:66px;position:relative;overflow:hidden}
.card.front{background:var(--paper);padding:7px 9px}
.card.front .brand{font-size:9px}
.card.front .name{font-size:6.5px;font-weight:700;color:var(--navy);margin-top:5px}
.card.front .title{font-size:4.8px;color:var(--green);font-weight:600}
.card.front .contact{font-size:4.2px;line-height:1.45;margin-top:3px;white-space:nowrap}
.card.back{background:var(--navy);display:flex;flex-direction:column;align-items:center;justify-content:center;gap:6px}
.card.back .brand{font-size:11px}
.card.back .web{font-size:5.5px;color:var(--paper);letter-spacing:.3px}

.folder{width:160px;height:212px;background:var(--navy);position:relative;display:flex;align-items:center;justify-content:center;overflow:hidden}
.folder .brand{font-size:16px}
.folder svg{position:absolute;left:0;bottom:0}

.disc{width:130px;height:130px;border-radius:50%;background:var(--navy);position:relative;display:flex;align-items:center;justify-content:center}
.disc::after{content:"";position:absolute;width:26px;height:26px;border-radius:50%;background:var(--stage);border:5px solid #d9dce3}
.disc .brand{font-size:10px;position:absolute;top:30px}
.slip{width:130px;height:70px;background:var(--paper);padding:8px;position:relative}
.slip .brand{font-size:9px}
.slip .band{position:absolute;left:0;right:0;bottom:0;height:10px;background:var(--green)}

.slide{width:220px;height:124px;background:var(--navy);position:relative;padding:14px;color:var(--paper);overflow:hidden}
.slide .thanks{font-size:20px;font-weight:600;line-height:1.1;position:absolute;right:16px;bottom:24px;text-align:right}
.slide .band{position:absolute;left:0;right:0;bottom:0;height:8px;background:var(--green)}
.slide .brand{font-size:11px}
.report{width:220px;height:78px;background:var(--paper);padding:9px;display:flex;gap:10px}
.report .bars{display:flex;align-items:flex-end;gap:5px;height:58px}
.report .bars span{width:12px;background:var(--navy)}
.report .bars span.g{background:var(--green)}
.report .lines{flex:1;display:flex;flex-direction:column;gap:5px;padding-top:4px}
.report .lines .line{height:2px;background:var(--muted)}
.report .lines .brand{font-size:9px;margin-bottom:4px}
</style>
</head>
<body>
<main class="sheet-set">

  <section class="letterhead">
    <div class="brand"><span class="dot"></span>nimbratek</div>
    <div class="body">
      <div class="line short"></div>
      <div class="line"></div><div class="line"></div><div class="line"></div>
      <div class="line short"></div>
      <div class="line"></div><div class="line"></div><div class="line short"></div>
    </div>
    <div class="footer">88 Harbor Lane, Suite 5, Riverton 40210<br>www.nimbratek.com</div>
  </section>

  <div class="col">
    <section class="envelope">
      <div class="brand"><span class="dot"></span>nimbratek</div>
      <div class="return">88 Harbor Lane, Suite 5<br>Riverton 40210</div>
      <div class="band"></div>
    </section>
    <div class="row">
      <section class="card front">
        <div class="brand"><span class="dot"></span>nimbratek</div>
        <div class="name">Ravi Mehlan</div>
        <div class="title">President &amp; CEO</div>
        <div class="contact">88 Harbor Lane, Suite 5, Riverton 40210<br>555-0142 ext 16<br>ravi@nimbratek.com</div>
      </section>
      <section class="card back">
        <div class="brand light"><span class="dot"></span>nimbratek</div>
        <div class="web">www.nimbratek.com</div>
      </section>
    </div>
  </div>

  <section class="folder">
    <div class="brand light"><span class="dot"></span>nimbratek</div>
    <svg width="160" height="60" viewBox="0 0 160 60">
      <path d="M0 30 Q80 0 160 24 L160 60 L0 60 Z" fill="var(--green)"/>
      <path d="M0 40 Q80 14 160 36 L160 60 L0 60 Z" fill="var(--paper)"/>
    </svg>
  </section>

  <div class="col">
    <section class="disc">
      <div class="brand light"><span class="dot"></span>nimbratek</div>
    </section>
    <section class="slip">
      <div class="brand"><span class="dot"></span>nimbratek</div>
      <div class="band"></div>
    </section>
  </div>

  <div class="col">
    <section class="slide">
      <div class="brand light"><span class="dot"></span>nimbratek</div>
      <div class="thanks">Thanks<br>for Coming</div>
      <div class="band"></div>
    </section>
    <section class="report">
      <div class="bars"><span style="height:22px"></span><span class="g" style="height:34px"></span><span style="height:46px"></span><span class="g" style="height:56px"></span></div>
      <div class="lines">
        <div class="brand"><span class="dot"></span>nimbratek</div>
        <div class="line"></div><div class="line"></div><div class="line" style="width:60%"></div>
      </div>
    </section>
  </div>

  <section class="letterhead">
    <div class="brand"><span class="dot"></span>nimbratek</div>
    <div class="body">
      <div class="line"></div><div class="line"></div><div class="line short"></div>
      <div class="line"></div><div class="line"></div><div class="line"></div>
      <div class="line short"></div>
    </div>
    <div class="footer">555-0142 ext 16<br>ravi@nimbratek.com</div>
  </section>

</main>
</body>
</html>
```